Business Card Design Project

for a second hand vintage clothing store. shop name is The Velvet Cupboard

Cards to be double sided

The name on the card is Joanna Whitfield

Information to put on card:

The Velvet Cupboard
Joanna Whitfield (no job title)
42/871 Dunmore St, Glenwick, Sydney, NSW, 2009.
Mobile: 0412 905 261
Email: thevelvetcupboard@mailbox.com.au
Web: www.thevelvetcupboard.com.au

Target Market(s)

Women looking at vintage clothing

Industry/Entity Type

Clothing

```html
<!DOCTYPE html>
<html lang="en">
<head>
<meta charset="utf-8">
<title>The Velvet Cupboard – Business Card</title>
<link rel="stylesheet" href="https://fonts.googleapis.com/css2?family=Source+Sans+3:wght@400;500;600&display=swap">
<style>
  :root {
    --paper: #ffffff;
    --maroon: #7d0a2b;
    --gold: #ecd79c;
    --shoe-rust: #8a3a22;
    --form-grey: #d9d6d2;
    --font-main: "Source Sans 3", "Myriad Pro", Arial, sans-serif;
  }
  html, body {
    margin: 0;
    padding: 0;
    overflow: hidden;
    background: var(--paper);
  }
  .card {
    position: relative;
    width: 1200px;
    height: 686px;
    background: var(--paper);
    font-family: var(--font-main);
    overflow: hidden;
  }
  .shop-name {
    position: absolute;
    left: 32px;
    top: 92px;
    margin: 0;
    font-size: 60px;
    font-weight: 400;
    line-height: 1;
    color: var(--gold);
    letter-spacing: 0.5px;
    white-space: nowrap;
  }
  .contact {
    position: absolute;
    left: 440px;
    top: 214px;
  }
  .contact p { margin: 0; line-height: 1; white-space: nowrap; }
  .owner-name {
    font-size: 44px;
    font-weight: 500;
    color: var(--maroon);
    letter-spacing: 0.3px;
  }
  .contact-lines {
    margin-top: 20px;
    font-size: 32px;
    color: var(--gold);
  }
  .contact-lines p { height: 43px; }
  .address {
    position: absolute;
    left: 438px;
    top: 413px;
    font-size: 32px;
    font-weight: 600;
    font-style: normal;
    color: var(--maroon);
    line-height: 38px;
  }
  .address p { margin: 0; white-space: nowrap; }
  .dress-form-art {
    position: absolute;
    left: 1002px;
    top: 400px;
    width: 60px;
    height: 62px;
  }
  .shoes-art {
    position: absolute;
    left: 945px;
    top: 506px;
    width: 176px;
    height: 104px;
  }
  .tagline {
    position: absolute;
    left: 904px;
    top: 465px;
    margin: 0;
    font-size: 37px;
    font-weight: 400;
    line-height: 1;
    color: var(--gold);
    white-space: nowrap;
  }
</style>
</head>
<body>
  <main class="card">
    <h1 class="shop-name">The Velvet Cupboard</h1>

    <section class="contact">
      <p class="owner-name">Joanna Whitfield</p>
      <div class="contact-lines">
        <p class="phone">0412.905.261 cell</p>
        <p class="email">thevelvetcupboard@mailbox.com.au</p>
        <p class="web">www.thevelvetcupboard.com.au</p>
      </div>
    </section>

    <address class="address">
      <p>42/871 Dunmore Street</p>
      <p>Glenwick, Sydney,</p>
      <p>NSW, 2009</p>
    </address>

    <svg class="dress-form-art" role="img" aria-label="Photo of a small wire dress form" viewBox="0 0 60 62">
      <rect width="60" height="62" rx="4" fill="var(--form-grey)"/>
    </svg>

    <p class="tagline">Vintage Clothing</p>

    <svg class="shoes-art" role="img" aria-label="Photo of a pair of rust suede vintage heels" viewBox="0 0 176 104">
      <defs>
        <linearGradient id="shoeTones" x1="0" y1="0" x2="0" y2="1">
          <stop offset="0" stop-color="#a0543a"/>
          <stop offset="1" stop-color="var(--shoe-rust)"/>
        </linearGradient>
      </defs>
      <rect width="176" height="104" rx="6" fill="url(#shoeTones)"/>
    </svg>
  </main>
</body>
</html>
```